New Website Design. Porjtect is Guaranteed.

I would like a site similar to this: http://givevehiclehope.org.

old site: http://www.wheelsforbloom.org

Create a professional website; a car donation site seeking leads to return calls.

Please see http://givevehiclehope.org for the concept I am after.

The webpage should have a professional feel. The pages to include are 'Home', 'About us' and 'Get Started'

Industry/Entity Type

It Professional

Coding

Coded - Design and coding required

Number of Pages Required

1 page

```html
<!DOCTYPE html>
<html lang="en">
<head>
<meta charset="utf-8">
<title>Drive For Dreams – Donate Your Car</title>
<link rel="stylesheet" href="https://fonts.googleapis.com/css2?family=Rajdhani:wght@500;600;700&family=Open+Sans:wght@400;600;700&display=swap">
<style>
:root{
  --navy:#1b3460;
  --navy-deep:#142a4f;
  --orange:#e06c14;
  --orange-card:rgba(214,110,30,.88);
  --form-bg:rgba(60,60,60,.9);
  --ink:#1d1d1d;
  --muted:#555;
  --faq-bg:#f3f3f3;
  --rule:#cfcfcf;
  --cream:#f6e3b0;
  --frame:#e9e9e9;
}
*{box-sizing:border-box;margin:0;padding:0}
html,body{width:1200px;height:2493px;overflow:hidden}
body{background:var(--frame);font-family:"Open Sans",Arial,sans-serif;color:var(--ink);position:relative}
.page{position:absolute;left:13px;top:0;width:1174px;height:2493px;background:#fff;overflow:hidden}
.abs{position:absolute}

/* top bar */
.topbar{left:590px;top:0;width:584px;height:55px;background:var(--navy);clip-path:polygon(18px 0,100% 0,100% 100%,0 100%,0 48px)}
.topbar-items{left:645px;top:0;height:55px;display:flex;align-items:center;gap:22px;color:#fff;font-size:15px;font-weight:600}
.topbar-items span{display:flex;align-items:center;gap:8px}
.social{display:flex;gap:6px}
.social i{display:block;width:20px;height:20px;border:2px solid #fff;border-radius:50%}

/* header */
.brand{left:40px;top:70px;font-family:"Rajdhani",sans-serif;font-weight:700;font-size:38px;color:var(--orange);letter-spacing:.3px}
.mainnav{right:18px;top:93px;display:flex;align-items:center;gap:26px;font-family:"Rajdhani",sans-serif;font-weight:700;font-size:17px;color:#111}
.mainnav .current{border-bottom:3px solid var(--orange);padding-bottom:2px}
.mainnav .cta{background:var(--orange);color:#fff;padding:6px 12px}

/* hero */
.hero{left:0;top:155px;width:1174px;height:510px;background:linear-gradient(180deg,#cfe3ef 0%,#e8f1f5 45%,#f6f8f8 100%)}
.hero-photo{left:20px;top:200px;width:760px;height:310px;background:linear-gradient(90deg,#e4e6e8,#d7d3d2 45%,#c9b7b5 100%);opacity:.85;border-radius:4px}
.hero-title{left:231px;top:80px;font-family:"Rajdhani",sans-serif;font-weight:700;font-size:33px;line-height:40px;color:var(--navy)}
.donate-form{left:753px;top:40px;width:387px;height:420px;background:var(--form-bg)}
.donate-form h2{height:39px;background:var(--orange);color:#fff;font-family:"Rajdhani",sans-serif;font-weight:700;font-size:20px;text-align:center;line-height:39px}
.donate-form p{margin:14px 30px 0;color:#fff;font-weight:700;font-size:15.5px;line-height:21px;text-align:center}
.fields{margin:14px 0 0 33px;width:323px;display:grid;grid-template-columns:153px 153px;gap:13px 17px}
.field{height:29px;background:#f4f4f4;border-radius:4px;font-size:12.5px;color:#666;padding:0 10px;line-height:29px;position:relative}
.field.wide{grid-column:1/3}
.field.select::after{content:"";position:absolute;right:10px;top:11px;border:5px solid transparent;border-top-color:#666}
.submit{margin:14px 0 0 33px;width:323px;height:47px;background:var(--orange);color:#fff;border-radius:5px;font-weight:700;font-size:19px;text-align:center;line-height:47px}

/* band */
.band{left:0;top:665px;width:1174px;height:78px;background:var(--navy);color:#fff;font-weight:700;font-size:22px;text-align:center;line-height:78px}

/* how it works */
.section-title{font-family:"Rajdhani",sans-serif;font-weight:600;color:var(--orange);text-align:center;width:1174px;left:0}
.how-title{top:806px;font-size:35px}
.step{top:880px;display:flex;gap:14px}
.step svg{flex:none}
.step-text{width:262px}
.step h3{font-size:16.5px;font-weight:700;color:#111;line-height:20px;white-space:nowrap}
.step p{font-size:12.5px;font-weight:600;color:#333;line-height:17px}
.step ul{list-style:none;margin-top:14px;font-size:12.5px;font-weight:600;color:#333;line-height:17px}

/* tax */
.tax{left:0;top:1060px;width:1174px;height:635px;background:linear-gradient(135deg,#2d4a7a 0%,#3d5f8f 40%,#5a7aa3 65%,#2a4470 100%)}
.tax-title{top:1120px;width:1174px;left:0;text-align:center;color:#fff;font-family:"Rajdhani",sans-serif;font-weight:700;font-size:34px}
.tax-sub{top:1170px;width:1174px;left:0;text-align:center;color:#fff;font-weight:700;font-size:13.5px}
.tax-card{top:1233px;width:307px;height:371px;background:var(--orange-card);border:2px solid #fff;border-radius:10px;color:#fff;font-size:13.2px;line-height:18.5px;padding:72px 16px 0 16px}
.tax-card h4{position:absolute;top:17px;left:50%;transform:translateX(-50%);background:var(--navy);border-radius:8px;padding:0 14px;height:40px;line-height:40px;font-size:13.5px;font-weight:700;white-space:nowrap}
.tax-card p+p{margin-top:18px}
.badge{position:absolute;bottom:-46px;left:50%;transform:translateX(-50%);width:96px;height:96px;border-radius:50%;background:#fff;border:3px solid #c9453a;display:flex;flex-direction:column;align-items:center;justify-content:center;color:var(--orange);font-weight:700;font-size:12.5px}

/* faq */
.faq{left:0;top:1695px;width:1174px;height:544px;background:var(--faq-bg)}
.faq-title{top:1755px;font-size:35px}
.faq-col{top:1830px;width:461px;list-style:none}
.faq-col li{border-bottom:1px solid var(--rule);padding:9px 0 8px 0;font-size:13.8px;font-weight:700;color:#111;line-height:19px}

/* footer */
.footer{left:0;top:2239px;width:1174px;height:208px;background:var(--navy)}
.footer-cream{left:727px;top:2239px;width:447px;height:208px;background:var(--cream);clip-path:polygon(124px 0,100% 0,100% 100%,0 100%)}
.footer h5{font-size:13px;font-weight:700;color:#fff;margin-bottom:10px}
.f-about{left:77px;top:2266px;width:270px;color:#fff;font-size:11.2px;font-weight:700;line-height:16px}
.f-about h5,.f-nav h5,.f-contact h5{font-size:13px;font-weight:700;color:#fff;margin-bottom:10px}
.f-nav{left:386px;top:2266px;color:#fff;font-size:11.2px;font-weight:700;line-height:19px;list-style:none}
.f-contact{left:534px;top:2266px;color:#fff;font-size:12.5px;font-weight:700;line-height:19px}
.f-contact .phone{display:flex;gap:12px}
.f-brand{left:880px;top:2334px;font-family:"Rajdhani",sans-serif;font-weight:700;font-size:34px;color:var(--orange)}
.copyright{left:0;top:2447px;width:1174px;height:46px;background:#fff;text-align:center;font-size:11px;font-weight:700;line-height:40px;color:#222}
</style>
</head>
<body>
<div class="page">

  <div class="abs topbar"></div>
  <div class="abs topbar-items">
    <span><svg width="20" height="20" viewBox="0 0 20 20"><circle cx="10" cy="10" r="9" fill="none" stroke="#fff" stroke-width="1.6"/><path d="M7 5.5l2 2-1 1.5a6 6 0 0 0 3 3l1.5-1 2 2-1.5 1.5c-3 0-7-4-7-7z" fill="#fff"/></svg>1-888-555-0147</span>
    <span><svg width="20" height="20" viewBox="0 0 20 20"><circle cx="10" cy="10" r="9" fill="none" stroke="#fff" stroke-width="1.6"/><rect x="5" y="6.5" width="10" height="7" fill="none" stroke="#fff" stroke-width="1.4"/><path d="M5 6.5l5 4 5-4" fill="none" stroke="#fff" stroke-width="1.4"/></svg>info@drivefordreams.org</span>
    <span class="social"><i></i><i></i><i></i></span>
  </div>

  <div class="abs brand">Drive For Dreams</div>
  <nav class="abs mainnav">
    <span class="current">HOME</span>
    <span>HOW IT WORKS</span>
    <span>ABOUT</span>
    <span class="cta">DONATE NOW</span>
  </nav>

  <section class="abs hero">
    <div class="abs hero-photo" role="img" aria-label="Photo of a white pickup truck and a red classic sports car with three happy children playing between them, city skyline behind"></div>
    <h1 class="abs hero-title">Donate Your Car for<br>Bright Hopes Foundation</h1>
    <form class="abs donate-form">
      <h2>MAKE A DONATION NOW</h2>
      <p>Donating is Easy &amp; Makes a Real Difference. Fill out the form below to instantly donate online.</p>
      <div class="fields">
        <div class="field">First Name</div>
        <div class="field">Last Name</div>
        <div class="field wide">Phone Number</div>
        <div class="field wide">Email Address</div>
        <div class="field select">Choose Year</div>
        <div class="field select">Choose Make</div>
        <div class="field">Vehicle Model</div>
        <div class="field">Zip Code</div>
      </div>
      <div class="submit">Click to Donate your Car</div>
    </form>
  </section>

  <div class="abs band">Donate Your Car, Truck, RV. Boat, Motorcycle, or ATV in all 50 states and make a difference.</div>

  <h2 class="abs section-title how-title">How It Works</h2>

  <div class="abs step" style="left:60px">
    <svg width="60" height="60" viewBox="0 0 60 60"><g fill="#e06c14"><rect x="6" y="6" width="8" height="6"/><rect x="18" y="6" width="34" height="6"/><rect x="6" y="18" width="8" height="6"/><rect x="18" y="18" width="34" height="6"/><rect x="6" y="30" width="8" height="6"/><rect x="18" y="30" width="34" height="6"/><path d="M10 40l14 6-6 2 5 7-3 2-5-7-4 5z"/></g></svg>
    <div class="step-text">
      <h3>1. Fill out the simple form</h3>
      <p>Use our online vehicle donation form to submit your information.</p>
      <ul><li>- Donating your vehicle is easy</li><li>- Vehicle donations accepted nationwide</li></ul>
    </div>
  </div>

  <div class="abs step" style="left:440px">
    <svg width="60" height="60" viewBox="0 0 60 60"><g fill="none" stroke="#e06c14" stroke-width="3"><path d="M6 40V26h18l6 8h14v6z"/><circle cx="14" cy="44" r="5"/><circle cx="38" cy="44" r="5"/><path d="M30 26l18-16M48 10v12"/></g><rect x="9" y="29" width="10" height="6" fill="#e06c14"/></svg>
    <div class="step-text">
      <h3>2. Schedule your free pick-up</h3>
      <p>We will arrange to pick up your vehicle when it is most convenient for you.</p>
      <ul><li>- Any vehicle is accepted</li><li>- Free towing for your charity vehicle<br>&nbsp;&nbsp;donation with 24 hours</li></ul>
    </div>
  </div>

  <div class="abs step" style="left:830px">
    <svg width="60" height="60" viewBox="0 0 60 60"><g fill="none" stroke="#e06c14" stroke-width="2.5"><rect x="14" y="6" width="32" height="46"/><path d="M10 10v46h32"/><path d="M20 36h20M20 42h20M26 36v12M34 36v12"/></g><text x="30" y="28" font-family="Open Sans,sans-serif" font-size="15" font-weight="700" fill="#e06c14" text-anchor="middle">$</text></svg>
    <div class="step-text" style="width:250px">
      <h3>3. Receive tax deduction</h3>
      <p>Once the vehicle donation is complete, you will receive your tax deductable vehicle donation receipt.</p>
    </div>
  </div>

  <section class="abs tax" role="img" aria-label="Blurred background photo of a person filling in tax paperwork, tinted blue"></section>
  <h2 class="abs tax-title">Tax Deduction Information For Your Car Donation</h2>
  <p class="abs tax-sub">The IRS has set the rules for the tax deduction of your vehicle donation</p>

  <article class="abs tax-card" style="left:37px">
    <h4>If Your Car Donation Sells for $500 Or Less</h4>
    <p>You can claim the fair market value of your vehicle up to and including $500, or the amount it is sold for if less than fair market value.</p>
    <p>When you donate your car, you will receive a tax deductible receipt to be submitted with your taxes.</p>
    <div class="badge">$500 or Less<svg width="44" height="16" viewBox="0 0 44 16"><path d="M2 12c0-4 6-5 10-5l6-4h12l6 4c4 0 6 2 6 5z" fill="#e06c14"/><circle cx="11" cy="13" r="3" fill="#fff" stroke="#e06c14" stroke-width="1.5"/><circle cx="33" cy="13" r="3" fill="#fff" stroke="#e06c14" stroke-width="1.5"/></svg></div>
  </article>

  <article class="abs tax-card" style="left:411px">
    <h4>If Your Car Donation Sells for $501 Or More</h4>
    <p>You can claim the exact amount for which the vehicle is sold. When you donate your car, we will provide you with a tax deductible receipt.</p>
    <p>Within 30 days from the sale of your vehicle we will provide you with a 1098-C form to submit with your taxes.</p>
    <div class="badge">$501 or More<svg width="44" height="16" viewBox="0 0 44 16"><path d="M2 12c0-4 6-5 10-5l6-4h12l6 4c4 0 6 2 6 5z" fill="#e06c14"/><circle cx="11" cy="13" r="3" fill="#fff" stroke="#e06c14" stroke-width="1.5"/><circle cx="33" cy="13" r="3" fill="#fff" stroke="#e06c14" stroke-width="1.5"/></svg></div>
  </article>

  <article class="abs tax-card" style="left:785px">
    <h4>How to File Your Taxes</h4>
    <p>To receive a tax deduction for a donated vehicle, you must include any charitable contributions itemized on Schedule A of Form 1040 from the IRS. Include your Charity Vehicle Gift tax-deductible receipt with your tax return. You do not need to submit Form 1098-C if your vehicle sells for less than $500 as your official Charity Vehicle Gift receipt is considered sufficient documentation by the IRS. If your vehicle sells for more than $500 but less than $5,000 you will need to submit the provided 1098-C form along with form 8283. ted vehicle.</p>
    <div class="badge"><svg width="46" height="46" viewBox="0 0 46 46"><path d="M6 18l17-12 17 12v22H6z" fill="#e06c14"/><rect x="12" y="10" width="22" height="20" fill="#fff"/><text x="23" y="25" font-family="Open Sans,sans-serif" font-size="13" font-weight="700" fill="#e06c14" text-anchor="middle">$</text><path d="M6 18l17 13 17-13" fill="none" stroke="#fff" stroke-width="2"/></svg></div>
  </article>

  <section class="abs faq"></section>
  <h2 class="abs section-title faq-title">Frequently Asked Questions</h2>
  <ul class="abs faq-col" style="left:96px">
    <li>+ What types of vehicles can be donated?</li>
    <li>+ If my vehicle is not running, can I still donate?</li>
    <li>+ What paperwork do I need to donate my vehicle?</li>
    <li>+ Is my donated vehicle tax -deductible?</li>
    <li>+ What areas do you service?</li>
    <li>+ What documents do I need to donate a car to charity?</li>
    <li>+ What if the vehicle is not registered in my name?</li>
    <li>+ There are two people listed on the title, what should I do?</li>
    <li>+ The Title Is In A Deceased Person's Name. How do I complete<br>&nbsp;&nbsp;&nbsp;The Transfer Of Title?</li>
  </ul>
  <ul class="abs faq-col" style="left:690px;width:414px">
    <li>+ How much will I receive as a tax deduction for my vehicle?</li>
    <li>+ How do you determine the value of my vehicle?</li>
    <li>+ When will I receive my tax receipt?</li>
    <li>+ How do I schedule a pick up?</li>
    <li>+ Who will pick up my vehicle?</li>
    <li>+ Do I have to be home when my vehicle is picked up?</li>
    <li>+ How quickly can my vehicle be picked up?</li>
    <li>+ Can you pick up my vehicle if it's not at my home?</li>
    <li>+ What will I receive at time of pick-up?</li>
  </ul>

  <footer>
    <div class="abs footer"></div>
    <div class="abs footer-cream"></div>
    <div class="abs f-about">
      <h5>About Vehicles For Hope</h5>
      We turn donated cars, trucks and boats into real support for children and families. Every gift is handled with care, from the first call to the final receipt, so your generosity goes as far as it possibly can.
    </div>
    <div class="abs f-nav">
      <h5>Navigation</h5>
      <ul style="list-style:none"><li>Home</li><li>How It works</li><li>About Us</li><li>Faq</li><li>Get Started</li></ul>
    </div>
    <div class="abs f-contact">
      <h5>Contact Info</h5>
      <div class="phone"><svg width="18" height="16" viewBox="0 0 18 16"><path d="M1 6c0-3 4-4 8-4s8 1 8 4v1h-4V5H5v2H1z" fill="#fff"/><rect x="3" y="8" width="12" height="7" rx="1" fill="#fff"/></svg><div>CALL 1-800-555-0192<br>Live Operators Available<br>7 Days A Week</div></div>
    </div>
    <div class="abs f-brand">Drive For Dreams</div>
    <div class="abs copyright">COPYRIGHT © 2017 VEHICLES FOR HOPE. ALL RIGHTS RESERVED.</div>
  </footer>

</div>
</body>
</html>
```